Billboard For Marcus Delvane

Need a Billboard 8ft. High x 16ft. Long. Ive attached a former billboard and looking for the same thing just updated with:
Wardens Guild Award Logo - 2020, 2022
Summit Lantern award Logo - 2022

Thanks.

```html
<!DOCTYPE html>
<html lang="en">
<head>
<meta charset="utf-8">
<title>Billboard – Marcus Delvane</title>
<link rel="stylesheet" href="https://fonts.googleapis.com/css2?family=Roboto:ital,wght@1,400&family=Jost:ital,wght@0,400;0,500;0,700;1,700&family=Oswald:wght@300;500&display=swap">
<style>
  :root {
    --backdrop: #d9dadb;
    --board: #ffffff;
    --ink: #111111;
    --muted: #333333;
    --brand-red: #dc1237;
    --brand-blue: #36549b;
  }
  * { margin: 0; padding: 0; box-sizing: border-box; }
  html, body {
    width: 1200px; height: 1200px; overflow: hidden;
    background: var(--backdrop);
  }
  .billboard {
    position: absolute;
    left: 75px; top: 337px;
    width: 1050px; height: 525px;
    background: var(--board);
    overflow: hidden;
  }
  .headline {
    position: absolute;
    left: 38px; top: 28px;
    font-family: "Roboto", sans-serif;
    font-style: italic; font-weight: 400;
    font-size: 90px; line-height: 82px;
    color: var(--ink);
    letter-spacing: 1px;
    white-space: nowrap;
  }
  .headline .accent { color: var(--brand-red); }
  .contact-frame {
    position: absolute;
    left: 40px; top: 244px;
    width: 629px; height: 142px;
    border: 2px solid var(--brand-red);
    border-radius: 10px;
  }
  .agent-name {
    position: absolute;
    left: 152px; top: 219px;
    width: 406px; height: 51px;
    background: var(--brand-red);
    border-radius: 8px;
    color: #fff;
    font-family: "Jost", sans-serif;
    font-weight: 500;
    font-size: 40px; line-height: 51px;
    text-align: center;
    letter-spacing: 0.5px;
  }
  .agent-title {
    position: absolute;
    left: 40px; top: 274px; width: 629px;
    text-align: center;
    font-family: "Jost", sans-serif;
    font-weight: 400; font-size: 25px;
    color: var(--muted);
    letter-spacing: 0.5px;
  }
  .agent-phone {
    position: absolute;
    left: 40px; top: 296px; width: 629px;
    text-align: center;
    font-family: "Jost", sans-serif;
    font-weight: 700; font-size: 83px; line-height: 90px;
    color: var(--brand-red);
    letter-spacing: 1px;
  }
  .tagline {
    position: absolute;
    left: 40px; top: 393px; width: 629px;
    text-align: center;
    font-family: "Jost", sans-serif;
    font-weight: 700; font-size: 29px;
    color: var(--brand-red);
    letter-spacing: 1px;
  }
  .tagline em { font-style: italic; }
  .award {
    position: absolute;
    display: flex; align-items: center; gap: 5px;
    font-family: "Oswald", sans-serif;
    color: var(--ink);
  }
  .award-summit { left: 155px; top: 456px; }
  .award-wardens { left: 341px; top: 451px; }
  .award-mark {
    border-radius: 50%;
    background: #1a1a1a;
    flex: none;
  }
  .award-summit .award-mark { width: 40px; height: 40px; }
  .award-wardens .award-mark { width: 56px; height: 56px; background: #fff; border: 2px solid #1a1a1a; }
  .award-brand { font-size: 8px; font-weight: 300; letter-spacing: 0.5px; line-height: 10px; }
  .award-title { font-size: 17px; font-weight: 300; line-height: 17px; }
  .award-wardens .award-title { font-weight: 500; font-size: 14px; line-height: 14px; }
  .award-row { display: flex; align-items: center; gap: 4px; }
  .award-note {
    font-size: 7px; font-weight: 300; line-height: 7px;
    border-left: 1px solid #1a1a1a; padding-left: 3px;
  }
  .award-years { font-size: 10px; font-weight: 500; line-height: 12px; letter-spacing: 0.5px; }
  .base-band {
    position: absolute;
    left: 0; top: 514px;
    width: 630px; height: 11px;
    background: var(--brand-blue);
  }
  .agent-portrait {
    position: absolute;
    left: 628px; top: 0;
    width: 422px; height: 525px;
  }
</style>
</head>
<body>
  <main class="billboard">
    <h1 class="headline">BUYING OR<br>SELLING? <span class="accent">CALL</span></h1>

    <div class="contact-frame"></div>
    <div class="agent-name">MARCUS DELVANE</div>
    <p class="agent-title">SALES REPRESENTATIVE.</p>
    <p class="agent-phone">613.555.0142</p>
    <p class="tagline">FOCUSED, DRIVEN AND <em>EXPERIENCED!</em></p>

    <div class="award award-summit">
      <span class="award-mark"></span>
      <div>
        <div class="award-brand">HARBOURLINE REALTY</div>
        <div class="award-title">SUMMIT LANTERN<br>AWARD 2022</div>
      </div>
    </div>

    <div class="award award-wardens">
      <span class="award-mark"></span>
      <div>
        <div class="award-brand">HARBOURLINE REALTY</div>
        <div class="award-title">WARDENS</div>
        <div class="award-row">
          <span class="award-title">GUILD</span>
          <span class="award-note">NATIONAL<br>TOP 1%</span>
        </div>
        <div class="award-years">2020 · 2022</div>
      </div>
    </div>

    <div class="base-band"></div>

    <svg class="agent-portrait" role="img" aria-label="Portrait photo of the sales representative in a blue shirt and patterned tie" viewBox="0 0 422 525">
      <defs>
        <linearGradient id="portraitTone" x1="0" y1="0" x2="0" y2="1">
          <stop offset="0" stop-color="#f3ede9"/>
          <stop offset="0.5" stop-color="#e4c9bd"/>
          <stop offset="0.75" stop-color="#3a55a6"/>
          <stop offset="1" stop-color="#2d4a9e"/>
        </linearGradient>
      </defs>
      <path d="M0 525 L60 380 L120 330 L160 10 L400 10 L422 300 L422 525 Z" fill="url(#portraitTone)"/>
    </svg>
  </main>
</body>
</html>
```